TIVARELCAP web-presence redisign

We would like to have our existing web-presence redesigned. Have a look at www.tivarel.ch (please use explorer). To the existing 11 pages we would add one more.

```html
<!DOCTYPE html>
<html lang="de">
<head>
<meta charset="utf-8">
<title>TIVARELCAP Zahnarztpraxis – Kontakt</title>
<link rel="stylesheet" href="https://fonts.googleapis.com/css2?family=Source+Sans+3:wght@400;600&display=swap">
<style>
:root{
  --dark:#333333;
  --header:#f1f1f1;
  --blue:#1b8fc3;
  --nav:#4cb9e3;
  --nav-active:#1c87ba;
  --content:#ebebeb;
  --lower:#f6f4f5;
  --text:#3d3d3d;
  --accent:#2a9ad0;
  --gold:#d9a21b;
  --field:#f6f6f6;
  --yellow:#f2d23a;
  --lang:#5cc3ec;
}
*{margin:0;padding:0;box-sizing:border-box}
html,body{width:939px;height:1200px;overflow:hidden}
body{position:relative;font-family:"Source Sans 3",sans-serif;color:var(--text);background:var(--lower)}
.abs{position:absolute}
.topbar{left:0;top:0;width:939px;height:33px;background:var(--dark)}
.topnav{top:12px;font-size:11px;color:#fff}
.topnav.home{color:var(--yellow)}
.topnav.lang{color:var(--lang)}
.search{left:721px;top:0;width:197px;height:33px;background:#6a6a6a;color:#fff;font-size:10px;padding:14px 12px}
.header{left:0;top:33px;width:939px;height:74px;background:var(--header)}
.social-box{left:721px;top:33px;width:195px;height:47px;background:#fff;border-radius:0 0 6px 6px;box-shadow:0 2px 3px rgba(0,0,0,.2)}
.social{top:40px;width:31px;height:31px;border-radius:6px;background:#8a98a6}
.logo-mark{left:34px;top:28px;width:44px;height:44px;border-radius:50%;background:var(--gold)}
.logo-name{left:86px;top:36px;font-size:30px;font-weight:600;color:#8b8b8b;letter-spacing:.5px}
.logo-sub{left:116px;top:66px;font-size:21px;color:#444}
.call{left:452px;top:42px;font-size:16px;font-weight:600;color:var(--accent)}
.call-num{left:452px;top:62px;font-size:16px;font-weight:600;color:#222}
.phone-icon{left:416px;top:44px}
.stripe{left:0;top:107px;width:939px;height:7px;background:var(--dark)}
.band{left:0;top:114px;width:939px;height:318px;background:var(--blue)}
.content{left:0;top:432px;width:939px;height:419px;background:var(--content)}
.mainnav{left:83px;top:94px;width:785px;height:35px;background:var(--nav);box-shadow:0 10px 8px -6px rgba(0,0,0,.45);z-index:2}
.mainnav a{position:absolute;top:10px;font-size:12.5px;color:#fff;text-decoration:none}
.mainnav .active{top:0;height:35px;width:123px;background:var(--nav-active);padding-top:10px;text-align:center}
.slider{left:29px;top:150px;width:887px;height:322px;background:linear-gradient(90deg,#cfd0ea 0%,#e2e3f1 40%,#e9dcd4 62%,#d9b7a4 80%,#c9b8c0 100%);box-shadow:0 12px 10px -8px rgba(0,0,0,.5);z-index:2}
.arrow{top:258px;width:26px;height:54px;background:#111;z-index:3}
.arrow-l{left:27px;border-radius:0 27px 27px 0}
.arrow-r{left:890px;border-radius:27px 0 0 27px}
.cap{left:29px;font-size:18px;font-weight:600;padding:5px 12px;z-index:3}
.cap1{top:341px;background:#111;color:#fff}
.cap2{top:394px;background:#fff;color:#111;padding:8px 13px}
h2{position:absolute;font-size:26px;font-weight:400;text-decoration:underline;text-underline-offset:4px;color:#444}
.lines{font-size:14.5px;line-height:25px;color:#444}
.field{left:551px;width:278px;height:29px;background:var(--field);font-size:12px;color:#999;padding:7px 11px}
.btn{top:809px;font-size:18px;letter-spacing:.5px}
.footer-line{left:0;top:1157px;width:939px;height:8px;background:var(--nav)}
.footer{left:0;top:1165px;width:939px;height:35px;background:var(--dark);color:#fff;font-size:10px}
.map{left:568px;top:907px;width:233px;height:154px;border:3px solid #999;background:linear-gradient(135deg,#f2d2a8,#f4e6a0 50%,#e8c7a3)}
</style>
</head>
<body>
<div class="abs topbar"></div>
<div class="abs topnav home" style="left:341px">HOME</div>
<div class="abs topnav" style="left:429px">Language :</div>
<div class="abs topnav lang" style="left:493px">English (UK)&nbsp;&nbsp;&nbsp;&nbsp;|&nbsp;&nbsp;&nbsp;&nbsp;&nbsp;German</div>
<div class="abs topnav" style="left:659px">Help</div>
<div class="abs search">Search . . .</div>

<div class="abs header"></div>
<div class="abs social-box"></div>
<div class="abs social" style="left:755px"></div>
<div class="abs social" style="left:791px"></div>
<div class="abs social" style="left:827px"></div>
<div class="abs social" style="left:863px"></div>

<div class="abs logo-mark"></div>
<div class="abs logo-name">TIVARELCAP</div>
<div class="abs logo-sub">Zahnarztpraxis</div>

<svg class="abs phone-icon" width="26" height="36" viewBox="0 0 26 36" aria-hidden="true">
  <path d="M9 2 L4 4 C0 12 0 24 4 32 L9 34 L12 27 L8 25 C7 20 7 16 8 11 L12 9 Z" fill="#555"/>
</svg>
<div class="abs call">Rufen Sie an für Beratung!</div>
<div class="abs call-num">301 - 555 -0142</div>

<div class="abs stripe"></div>
<div class="abs band"></div>
<div class="abs content"></div>

<nav class="abs mainnav">
  <a style="left:112px">HOME</a>
  <a style="left:202px">ZAHNMEDIZIN&nbsp;▾</a>
  <a style="left:338px">DENTALHYGIENE</a>
  <a style="left:486px">TEAM</a>
  <a class="active" style="left:534px">KONTAKT</a>
</nav>

<div class="abs slider" role="img" aria-label="Slider photo: smiling woman holding a green apple over a soft lilac floral background"></div>
<div class="abs arrow arrow-l"></div>
<div class="abs arrow arrow-r"></div>
<div class="abs cap cap1">"In bietet persönliche Betreuung mit den</div>
<div class="abs cap cap2">neuesten Fortschritten in der Zahnmedizin verpflichtet"</div>

<h2 style="left:49px;top:513px">Kontakt :</h2>
<div class="abs lines" style="left:51px;top:558px">
  TIVARELCAP Zahnarztpraxis<br>
  Dr. med. dent. Lena Marbach-Kessler<br>
  Lindenweg 12<br>
  CH-8600 Dorfbach<br><br>
  Tel: +41 (0)44 555 01 23<br>
  E-mail: info@tivarel.ch
</div>

<h2 style="left:547px;top:513px">Quick Kontakt :</h2>
<div class="abs field" style="top:562px">Name</div>
<div class="abs field" style="top:605px">Email</div>
<div class="abs field" style="top:647px">Ph</div>
<div class="abs field" style="top:689px;height:110px">Message</div>
<div class="abs btn" style="left:660px;color:#555">RESET</div>
<div class="abs btn" style="left:744px;color:var(--accent)">SUBMIT</div>

<h2 style="left:49px;top:863px">So finden Sie uns:</h2>
<div class="abs lines" style="left:51px;top:907px">
  Nordstadt Bahnhof nach Dorfbach mit S5 oder S15 in 14 Minuten (Gleis 23/24)<br>
  Seefeld nach Dorfbach mit S5 oder S15 in 21 Minuten (Gleis 5)
</div>
<h2 style="left:562px;top:863px">Map:</h2>
<div class="abs map" role="img" aria-label="Street map showing the route from the train station to the practice"></div>

<div class="abs footer-line"></div>
<svg class="abs" style="left:464px;top:1164px" width="22" height="11" viewBox="0 0 22 11" aria-hidden="true"><path d="M0 0 H22 L11 11 Z" fill="#4cb9e3"/></svg>
<div class="abs footer"></div>
<div class="abs" style="left:26px;top:1174px;color:#fff;font-size:10px">Home&nbsp; |&nbsp; Zahnmedizin&nbsp; |&nbsp; Dentalhygiene&nbsp; |&nbsp; Team&nbsp; |&nbsp; Kontakt</div>
<div class="abs" style="left:759px;top:1174px;color:#fff;font-size:10px">2014 Tivarelcap Zahnarztpraxis.com</div>
</body>
</html>
```